Crumb Joy pastry business card design

I need a logo and a business card design for my baking business, "Crumb Joy". I daily bake French pastries from scratch using high quality ingredients and directly cater to local customers. My product is very authentic but sold at a casual setting . I'm looking for a simple, cute, stylish yet earthy design. Like this kind of feel:
http://clipvault-demo.net/70416238
Target Market(s)
Metropolitan food conscious consumers in their 20-40s
Industry/Entity Type
Business
Requirements
Must have
- Soft pastel colors or other types of color schemes that would remind French pastries.
email: welovecrumbles@mailbox-example.net
twitter@crumbjoyla
www.crumbjoyla.net
Nice to have
Should not have
- pictures of pastries - sketches are ok.

```html
<!DOCTYPE html>
<html lang="en">
<head>
<meta charset="utf-8">
<title>Crumb Joy – Business Card</title>
<link rel="stylesheet" href="https://fonts.googleapis.com/css2?family=Poiret+One&display=swap">
<style>
  :root {
    --stage: #ece8e1;
    --cocoa: #3a1f1a;
    --cream: #ddd6c0;
    --white: #ffffff;
    --crust-light: #c98f63;
    --crust-mid: #a06a55;
    --plum: #6d4350;
    --plum-deep: #4a2c35;
  }
  * { margin: 0; padding: 0; box-sizing: border-box; }
  html, body {
    width: 1200px;
    height: 880px;
    overflow: hidden;
    background: var(--stage);
  }
  .canvas {
    position: relative;
    width: 1200px;
    height: 880px;
    font-family: "Poiret One", sans-serif;
  }
  .card {
    position: absolute;
    top: 286px;
    width: 540px;
    height: 308px;
    overflow: hidden;
    box-shadow: 0 10px 24px rgba(40, 25, 20, 0.22);
  }

  /* Back side: contact details */
  .card--back {
    left: 40px;
    background: var(--cocoa);
    color: var(--cream);
  }
  .contact-list {
    list-style: none;
    position: absolute;
    left: 66px;
    top: 78px;
  }
  .contact-item {
    display: flex;
    align-items: center;
    height: 34px;
    margin-bottom: 10px;
    font-size: 19px;
    letter-spacing: 1.5px;
    text-transform: uppercase;
  }
  .contact-icon {
    width: 24px;
    height: 20px;
    margin-right: 22px;
    flex-shrink: 0;
  }
  .corner-scallop {
    position: absolute;
    right: 0;
    bottom: 0;
    width: 110px;
    height: 90px;
  }

  /* Front side: name and web address */
  .card--front {
    left: 620px;
  }
  .front-backdrop {
    position: absolute;
    inset: 0;
    background:
      radial-gradient(ellipse at 70% 55%, rgba(201, 143, 99, 0.85) 0%, rgba(201, 143, 99, 0) 55%),
      linear-gradient(160deg, var(--plum) 0%, var(--crust-mid) 45%, var(--crust-light) 70%, var(--plum-deep) 100%);
  }
  .brand-name {
    position: absolute;
    left: 0;
    right: 0;
    top: 104px;
    text-align: center;
    color: var(--white);
    font-size: 64px;
    font-weight: 400;
    letter-spacing: 10px;
    text-transform: uppercase;
  }
  .brand-web {
    position: absolute;
    left: 0;
    right: 0;
    top: 212px;
    text-align: center;
    color: var(--white);
    font-size: 19px;
    letter-spacing: 2px;
    text-transform: uppercase;
  }
</style>
</head>
<body>
<main class="canvas">

  <section class="card card--back" aria-label="Business card back">
    <ul class="contact-list">
      <li class="contact-item">
        <svg class="contact-icon" viewBox="0 0 24 20" aria-hidden="true">
          <rect x="1" y="3" width="22" height="14" fill="var(--cream)"/>
          <path d="M1 3 L12 11 L23 3" fill="none" stroke="var(--cocoa)" stroke-width="1.4"/>
          <path d="M1 17 L9 9 M23 17 L15 9" fill="none" stroke="var(--cocoa)" stroke-width="1"/>
        </svg>
        <span>welovecrumbles@mailbox-example.net</span>
      </li>
      <li class="contact-item">
        <svg class="contact-icon" viewBox="0 0 24 20" aria-hidden="true">
          <rect x="3" y="0" width="18" height="18" rx="3" fill="var(--cream)"/>
        </svg>
        <span>@crumbjoyla</span>
      </li>
      <li class="contact-item">
        <svg class="contact-icon" viewBox="0 0 24 20" aria-hidden="true">
          <circle cx="12" cy="10" r="9" fill="var(--cream)"/>
          <g fill="none" stroke="var(--cocoa)" stroke-width="1">
            <ellipse cx="12" cy="10" rx="4" ry="9"/>
            <line x1="3" y1="10" x2="21" y2="10"/>
            <line x1="12" y1="1" x2="12" y2="19"/>
            <path d="M5 5 H19 M5 15 H19"/>
          </g>
        </svg>
        <span>www.crumbjoyla.net</span>
      </li>
    </ul>
    <svg class="corner-scallop" viewBox="0 0 110 90" aria-hidden="true">
      <g fill="var(--cream)">
        <circle cx="30" cy="70" r="22"/>
        <circle cx="42" cy="40" r="22"/>
        <circle cx="72" cy="24" r="24"/>
        <circle cx="100" cy="20" r="20"/>
        <rect x="30" y="40" width="80" height="50"/>
        <rect x="72" y="20" width="38" height="30"/>
      </g>
    </svg>
  </section>

  <section class="card card--front" aria-label="Business card front">
    <div class="front-backdrop" role="img" aria-label="Photo of a baked pastry tart in warm plum and golden crust tones"></div>
    <h1 class="brand-name">Crumb Joy</h1>
    <p class="brand-web">www.crumbjoyla.net</p>
  </section>

</main>
</body>
</html>
```